The Halvering House Letter/ Envelope

We need a letter and corresponding envelope designed for The Halvering House's end of year holiday material. The Halvering House (https://thehalveringhouse.org/) is a drug and alcohol addiction treatment center. I have their style guide attached, along with their letter and envelope from last year. Please use the same content as a placeholder for your new designs.

This is a large initiative to gather donations for the end of the calendar year. We want the creative to reflect the website design, and not be holiday-themed. We would also like to generate, and include, a QR code to link to the donation page on their new website - https://thehalveringhouse.org/quietly-give/

```html
<!DOCTYPE html>
<html lang="en">
<head>
<meta charset="utf-8">
<title>The Halvering House – Holiday Letter and Envelope</title>
<link rel="stylesheet" href="https://fonts.googleapis.com/css2?family=Lato:ital,wght@0,300;0,400;0,700;1,400&family=Fira+Sans:ital,wght@1,600&display=swap">
<style>
  :root {
    --brand-blue: #27aee0;
    --brand-blue-deep: #1c9bd0;
    --ink: #222222;
    --ink-soft: #777777;
    --paper: #ffffff;
    --backdrop: #eef3f6;
    --blush: #fbe0e2;
  }
  * { box-sizing: border-box; margin: 0; padding: 0; }
  html, body { width: 881px; height: 1200px; overflow: hidden; }
  body { background: var(--backdrop); font-family: "Lato", sans-serif; position: relative; }

  .envelope { position: absolute; left: 123px; top: 61px; width: 636px; height: 423px; background: var(--paper); overflow: hidden; }
  .envelope .snow-accent-top { position: absolute; left: 230px; top: 0; width: 140px; height: 115px; border-radius: 50%;
    background: radial-gradient(circle, var(--blush) 0%, rgba(251,224,226,0) 70%); }
  .envelope .snow-accent-corner { position: absolute; left: 465px; top: 250px; width: 200px; height: 200px; border-radius: 50%;
    background: radial-gradient(circle, var(--blush) 0%, rgba(251,224,226,0) 70%); }
  .brand-mark { position: absolute; display: flex; align-items: center; gap: 8px; color: var(--brand-blue); font-weight: 700; line-height: 1.05; }
  .brand-mark .brand-square { background: var(--brand-blue); flex: none; }
  .envelope .brand-mark { left: 50px; top: 60px; font-size: 21px; width: 200px; }
  .envelope .brand-mark .brand-square { width: 22px; height: 22px; }
  .envelope-banner { position: absolute; left: 0; top: 348px; width: 441px; height: 40px; background: var(--brand-blue);
    color: #fff; font-family: "Fira Sans", sans-serif; font-style: italic; font-weight: 600; font-size: 19px; line-height: 40px; padding-left: 39px; }

  .letter { position: absolute; left: 216px; top: 517px; width: 449px; height: 635px; background: var(--paper); overflow: hidden; }
  .letter-edge { position: absolute; left: 0; top: 0; width: 14px; height: 100%; }
  .letter .brand-mark { left: 360px; top: 40px; font-size: 10px; width: 80px; gap: 5px; }
  .letter .brand-mark .brand-square { width: 12px; height: 12px; }
  .letter-head { position: absolute; left: 25px; top: 34px; font-size: 6.5px; color: var(--ink); line-height: 9px; }
  .letter-head .date { margin-bottom: 8px; }
  .letter-body { position: absolute; left: 25px; top: 110px; width: 415px; font-size: 6.2px; line-height: 9px; color: var(--ink-soft); font-weight: 300; }
  .letter-body p { margin-bottom: 9px; }
  .letter-body .lead { color: var(--ink); font-weight: 400; }
  .letter-body .lead b { font-weight: 400; }
  .letter-body .sign-name { font-style: italic; color: var(--ink); font-weight: 400; }
  .letter-footer { position: absolute; left: 0; bottom: 13px; width: 100%; height: 20px; background: var(--brand-blue);
    color: #fff; font-size: 7px; line-height: 20px; text-align: center; }
</style>
</head>
<body>
  <section class="envelope" aria-label="Envelope">
    <div class="snow-accent-top" role="img" aria-label="Soft pink snowflake decoration"></div>
    <div class="snow-accent-corner" role="img" aria-label="Soft pink snowflake decoration"></div>
    <div class="brand-mark"><span class="brand-square"></span><span>The Halvering House</span></div>
    <div class="envelope-banner">Children are having a mental health crisis.</div>
  </section>

  <section class="letter" aria-label="Donation letter">
    <svg class="letter-edge" viewBox="0 0 14 635" preserveAspectRatio="none" aria-hidden="true">
      <rect width="14" height="635" fill="#27aee0"/>
      <polygon points="0,118 14,108 14,113 0,123" fill="#fff"/>
      <polygon points="0,186 14,176 14,181 0,191" fill="#fff"/>
      <polygon points="0,254 14,244 14,249 0,259" fill="#fff"/>
      <polygon points="0,322 14,312 14,317 0,327" fill="#fff"/>
      <polygon points="0,390 14,380 14,385 0,395" fill="#fff"/>
      <polygon points="0,458 14,448 14,453 0,463" fill="#fff"/>
    </svg>
    <div class="brand-mark"><span class="brand-square"></span><span>The Halvering House</span></div>

    <div class="letter-head">
      <p class="date">Date</p>
      <p>&lt;&lt;First_Name&gt;&gt; &lt;&lt;Last_Name&gt;&gt;</p>
      <p>&lt;&lt;Address1&gt;&gt;</p>
      <p>&lt;&lt;Address2&gt;&gt;</p>
      <p>&lt;&lt;City_State_Zip&gt;&gt;</p>
    </div>

    <div class="letter-body">
      <p>You can give the gift of love and support this holiday season and brighten the lives of children who come to the Hope Group. Just $50 one session for a child in need.</p>
      <p>It started with a phone call to Renata and Owen. “These kids need to go somewhere. Would you take them for just 30 days to prevent foster care?”</p>
      <p class="lead">Tessa and Junie, two sisters aged 9 and 5, needed a place to stay. Their parents were struggling. Addiction. Domestic violence. Self-harm. And neglect of the girls. The details were hard to hear.</p>
      <p>Renata and Owen first came to know Tessa and Junie by offering respite care one week every month for the girls and their parents. The program helped kids from entering foster care.</p>
      <p>Now they were being asked to take the girls for 30 days while Mom went to rehab and Dad was in jail. (Sadly, it’s been nearly a year because Mom kept putting it off.)</p>
      <p>How could they say no? Renata and Owen said yes, hoping to give these two young girls a break from the chaos. “We loved them. We had to keep them.”</p>
      <p>I’m reaching out to you today, not only to share their story, but to offer you a chance to be part of a beautiful journey. Tessa and Junie are two bright, beautiful girls who’ve faced more than any child should.</p>
      <p class="lead">The Halvering House needs caring, compassionate people like you to support kids like Tessa and Junie. People like you who want to be sure that kids affected by their parents’ addictions can get the support they need. Please, will you send your best donation right now?</p>
      <p>Tessa had witnessed the trauma up close, while Junie had been relatively shielded. But no matter the extent of their experiences, the impact was deep. From comments about self-harm to intense emotional breakdowns, their young hearts bore scars many of us can’t even imagine.</p>
      <p><span class="lead">Just 3 weeks after moving in with Renata and Owen, Tessa was introduced to the Hope Group at The Halvering House.</span> Although the first days were challenging, with Tessa retreating into herself, she soon started to bloom. Because of you, she learned to voice her feelings, articulate her fears, and began a path to healing.</p>
      <p><span class="lead">Junie wasn’t far behind. Under the guidance of Delia, one of our dedicated play therapists, she too started navigating her emotions.</span> As Renata, their foster mom fondly recounts, Junie has now become an expert at voicing her feelings, saying things like, “you’re making me mad and angry and disappointed.”</p>
      <p class="lead">&lt;&lt;First Name&gt;&gt; stories like these aren’t rare. But the resources, sadly, are. But, just $50 can provide one crucial therapy session for a child in need. Will you send in a gift right now?</p>
      <p>As the year closes and the season of giving begins, I’m reaching out to compassionate souls like you. With your generous donation, we can ensure that kids like Tessa and Junie can continue to find their voices, confront their traumas, and move toward brighter futures. And these two precious girls can continue on their journey here at The Halvering House.</p>
      <p>Our mission at The Halvering House is more than just recovery. It’s about rekindling joy, rebuilding lives, and rejuvenating souls. Will you join us on this journey?</p>
      <p>In the spirit of hope and healing,<br><span class="sign-name">Dorothea Whitcombe | CEO</span></p>
      <p class="lead">P.S. &lt;&lt;First Name&gt;&gt;, by choosing to donate today, you’re not only supporting The Halvering House but you’re also embracing children like Tessa and Junie, offering them a brighter, safer, and more hopeful tomorrow. Every dollar you give counts towards a new beginning. Please, send in your most generous gift today.</p>
    </div>

    <div class="letter-footer">The Halvering House | 412 Linden Row | Greenfield, OH 45123 | 555-014-2290 | www.thehalveringhouse.org</div>
  </section>
</body>
</html>
```